My portfolio needs a makeover! Clean, modern portfolio website needed for tech professional

I need a modern, updated design for my existing portfolio site (https://marelovic.folioshelf.example/). I am a content professional who has done a lot of different types of content work for big companies. I don't really have a title.

I want to stay simple and clean, but also can be a little whimsical, fun, and a little colorful to go along with the logo I just selected.

I have a domain on Pageloom (marelovic.com), but I’d be willing to move my domain to another site for the right design.

I would like it coded/configured and deployed, but I need the ability to update the site myself later to easily switch out my portfolio pieces. I’m not very good at html/xml.

Pages needed:
Home page
Who I am
How to reach me
What I do > By Craft (in the nav, this will be a dropdown under What I Do)
What I do > By Brand (in the nav, this will be a dropdown under What I Do)

Please see Website Design Doc for details!

Requirements
Must have
• Design must include these pages:
1. Homepage
2. Who I Am
3. What I Do
- By Brand
- By Craft
4. How to Reach Me
Nice to have
• Example portfolio sites I like:
https://www.drivenquarry.example/
http://jolesumner.example/
https://www.tdvarnock.example/
https://www.oriannebelcastro.example/

For my portfolio pieces, I like either tiles or a carousel.

```html
<!DOCTYPE html>
<html lang="en">
<head>
<meta charset="utf-8">
<title>Mare Lovic — By Craft</title>
<link rel="stylesheet" href="https://fonts.googleapis.com/css2?family=Montserrat:wght@400;500;700;800&family=Open+Sans:wght@400&display=swap">
<style>
  :root {
    --ink: #000;
    --white: #fff;
    --brand-blue: #2ea3dc;
    --nav-text: #e6e6e6;
    --body-text: #555;
    --footer-bg: #ececec;
    --footer-text: #333;
  }
  * { margin: 0; padding: 0; box-sizing: border-box; }
  html, body { width: 1200px; height: 875px; overflow: hidden; background: var(--white); }
  body { position: relative; font-family: "Montserrat", sans-serif; }

  .site-header { position: absolute; left: 0; top: 0; width: 1200px; height: 116px; background: var(--ink); }
  .brand { position: absolute; left: 86px; top: 48px; display: flex; align-items: center; gap: 8px; }
  .brand-dot { width: 12px; height: 12px; border-radius: 50%; background: var(--brand-blue); }
  .brand-name { font-weight: 700; font-size: 22px; letter-spacing: 0.5px; color: var(--brand-blue); }

  .main-nav a, .footer-nav a { position: absolute; text-decoration: none; white-space: nowrap; }
  .main-nav a { top: 55px; font-size: 14.6px; font-weight: 400; color: var(--nav-text); letter-spacing: 0.2px; }
  .main-nav a.is-home { font-weight: 700; color: #cfcfcf; }
  .nav-active-bar { position: absolute; left: 629px; top: 113px; width: 101px; height: 3px; background: var(--white); }
  .social-ring { position: absolute; }

  .section-title { position: absolute; left: 0; width: 1176px; top: 184px; text-align: center; font-size: 46px; font-weight: 500; color: var(--ink); letter-spacing: 0.5px; }
  .title-rule { position: absolute; left: 560px; top: 244px; width: 75px; height: 4px; background: var(--brand-blue); }

  .craft-card { position: absolute; top: 300px; width: 336px; }
  .craft-photo { position: relative; width: 336px; height: 329px; display: flex; align-items: center; justify-content: center; padding-top: 36px; }
  .craft-photo--publishing { background: linear-gradient(150deg, #6b5443 0%, #3b352f 45%, #1e2228 100%); }
  .craft-photo--writing { background: linear-gradient(160deg, #c9b6a0 0%, #a98f76 50%, #8c7560 100%); }
  .craft-photo--creative { background: linear-gradient(155deg, #b7b2aa 0%, #8d8a86 45%, #3c3a38 100%); }
  .craft-label { font-weight: 800; font-size: 25px; line-height: 27px; color: var(--white); text-align: center; text-transform: uppercase; }
  .craft-text { margin-top: 20px; font-family: "Open Sans", sans-serif; font-size: 12.7px; line-height: 19.3px; color: var(--body-text); text-align: center; }

  .site-footer { position: absolute; left: 0; top: 793px; width: 1200px; height: 82px; background: var(--footer-bg); }
  .footer-nav a { top: 31px; font-size: 11.6px; color: var(--footer-text); }
  .copyright { position: absolute; right: 182px; top: 29px; white-space: nowrap; text-align: right; font-family: "Open Sans", sans-serif; font-size: 13px; color: var(--footer-text); }
</style>
</head>
<body>
  <header class="site-header">
    <div class="brand"><span class="brand-dot"></span><span class="brand-name">MARE LOVIC</span></div>
    <nav class="main-nav">
      <a class="is-home" style="left:369px" href="#">HOME</a>
      <a style="left:473px" href="#">WHAT AM I DO</a>
      <a style="left:641px" href="#">WHAT I DO</a>
      <a style="left:780px" href="#">HOW TO REACH ME</a>
    </nav>
    <div class="nav-active-bar"></div>
    <svg class="social-ring" style="left:1026px;top:54px" width="30" height="30" viewBox="0 0 30 30" aria-label="Social profile">
      <circle cx="15" cy="15" r="13.5" fill="none" stroke="#fff" stroke-width="1.5"/>
    </svg>
  </header>

  <main>
    <h1 class="section-title">BY CRAFT</h1>
    <div class="title-rule"></div>

    <article class="craft-card" style="left:61px">
      <div class="craft-photo craft-photo--publishing" role="img" aria-label="Photo of people working on laptops at a shared desk">
        <span class="craft-label">Publishing &amp;<br>Production</span>
      </div>
      <p class="craft-text">Praesent sit amet est In dictum dolor eu dictum porttitor enim felis viverra mi eget luctus massa puruPraesent sit amet est In dictum dolor eu dictum porttitor</p>
    </article>

    <article class="craft-card" style="left:433px">
      <div class="craft-photo craft-photo--writing" role="img" aria-label="Photo of many open books laid out side by side">
        <span class="craft-label">Writing &amp;<br>Editing</span>
      </div>
      <p class="craft-text">Praesent sit amet est In dictum dolor eu dictum porttitor enim felis viverra mi eget luctus massa puruPraesent sit amet est In dictum dolor eu dictum porttitor</p>
    </article>

    <article class="craft-card" style="left:804px">
      <div class="craft-photo craft-photo--creative" role="img" aria-label="Overhead photo of hands typing on a laptop showing a photo gallery">
        <span class="craft-label">Creative &amp;<br>Branded</span>
      </div>
      <p class="craft-text">Praesent sit amet est In dictum dolor eu dictum porttitor enim felis viverra mi eget luctus massa puruPraesent sit amet est In dictum dolor eu dictum porttitor</p>
    </article>
  </main>

  <footer class="site-footer">
    <nav class="footer-nav">
      <a style="left:129px" href="#">HOME</a>
      <a style="left:210px" href="#">WHAT AM I DO</a>
      <a style="left:342px" href="#">WHAT I DO</a>
      <a style="left:451px" href="#">HOW TO REACH ME</a>
    </nav>
    <p class="copyright">© 2020 Lovic Studio All Right Reserved</p>
    <svg class="social-ring" style="left:1068px;top:23px" width="30" height="30" viewBox="0 0 30 30" aria-label="Social profile">
      <circle cx="15" cy="15" r="13.5" fill="none" stroke="#333" stroke-width="1.5"/>
    </svg>
  </footer>
</body>
</html>
```